Velvet Basin Suites, a portable luxury restroom trailer company needs a landing page

We need a landing page for a luxury portable restroom trailer company. This should be modern, and simple - use any combination of Pantone colors: Warm Gray 1C, Black 7C, 7529c, 873C, 8003C

We rent these trailers for special events like weddings, private parties, festivals, family reunions, team building, wine tastings, beer tastings, food truck round-ups, etc.

An idea of the landing page is in the files below. Please use stock photography and placeholder text for now. The winning design will be given final content.

Requirements
Must have
• Multiple "Get Quote" buttons or a place for them to type in type of rental, how many people etc

```html
<!DOCTYPE html>
<html lang="en">
<head>
<meta charset="utf-8">
<title>Velvet Basin Suites</title>
<link href="https://fonts.googleapis.com/css2?family=Poppins:wght@300;400;500;600;700;800&display=swap" rel="stylesheet">
<style>
:root{
  --blue:#2a5196;
  --blue-dark:#1f3f7a;
  --ink:#333;
  --muted:#666;
  --line:#4a4a4a;
  --footer:#24272c;
  --white:#fff;
}
*{box-sizing:border-box;margin:0;padding:0}
html,body{width:1200px;height:3148px;overflow:hidden}
body{position:relative;font-family:'Poppins',sans-serif;color:var(--ink);background:var(--white)}
.abs{position:absolute}
.center{left:0;width:1200px;text-align:center}

/* header */
.site-header{position:absolute;left:0;top:0;width:1200px;height:78px;background:#fff}
.brand{position:absolute;left:110px;top:22px;font-weight:700;font-size:26px;color:var(--blue);letter-spacing:-.3px}
.nav{position:absolute;top:30px;font-size:15.5px;color:#222}
.nav.active{color:var(--blue)}
.call-icon{position:absolute;left:815px;top:20px;width:40px;height:40px;border:1.5px solid var(--blue);border-radius:50%}
.call-icon svg{position:absolute;left:11px;top:11px}
.call-text{position:absolute;left:863px;top:30px;font-size:15.5px;color:#222}

/* hero */
.hero{position:absolute;left:0;top:78px;width:1200px;height:539px;background:var(--blue)}
.hero-cell{position:absolute}
.hero-overlay{position:absolute;left:271px;top:220px;width:658px;height:274px;background:rgba(20,20,25,.72)}
.hero-title{position:absolute;top:240px;font-weight:700;font-size:44px;color:#fff}
.hero-text{position:absolute;top:306px;left:315px;width:570px;text-align:center;font-size:16.5px;line-height:30px;color:#fff}
.btn-start{position:absolute;left:497px;top:411px;width:206px;height:51px;background:var(--blue);color:#fff;font-size:16px;font-weight:500;display:flex;align-items:center;justify-content:center;gap:8px}

/* section heads */
.sec-title{position:absolute;font-weight:700;font-size:42px;color:var(--blue)}
.sec-rule{position:absolute;left:567px;width:66px;height:4px;background:var(--blue)}
.sec-text{position:absolute;left:240px;width:720px;text-align:center;font-size:14.5px;line-height:25.5px;color:#333}

/* events */
.event-card{position:absolute;top:850px;width:232px;height:302px;border-radius:6px;box-shadow:0 2px 6px rgba(0,0,0,.25)}
.event-name{position:absolute;top:1166px;width:232px;text-align:center;font-size:16px;font-weight:500;color:var(--blue)}
.arrow-btn{position:absolute;top:969px;width:50px;height:49px;border:1px solid #555;background:#fff}
.arrow-btn svg{position:absolute;left:18px;top:17px}

/* products */
.products-band{position:absolute;left:0;top:1262px;width:1200px;height:670px;background:linear-gradient(180deg,#2a5297 0%,#25498a 60%,#2b5398 100%)}
.product-card{position:absolute;top:1481px;width:311px;height:350px;background:#fff;border-radius:6px}
.product-img{position:absolute;top:20px;border-radius:3px}
.product-name{position:absolute;top:210px;left:0;width:100%;text-align:center;font-size:20px;font-weight:500;color:var(--blue)}
.product-text{position:absolute;top:248px;left:12px;right:12px;text-align:center;font-size:13px;line-height:25.5px;color:#444}
.dot{position:absolute;top:1869px;width:14px;height:14px;border:2px solid #fff;border-radius:50%}
.dot.on{background:#fff}

/* form */
.field{position:absolute;border-bottom:2px solid var(--line);height:40px}
.field span{position:absolute;left:0;top:6px;font-size:15.5px;color:#666;font-weight:300}
.field svg{position:absolute;right:14px;top:12px}
.btn-send{position:absolute;left:501px;top:2655px;width:198px;height:52px;border-radius:26px;background:var(--blue);color:#fff;font-size:15.5px;font-weight:600;display:flex;align-items:center;justify-content:center;box-shadow:0 3px 6px rgba(0,0,0,.25)}

/* footer */
.site-footer{position:absolute;left:0;top:2763px;width:1200px;height:385px;background:linear-gradient(180deg,#2a2d33,#1f2227)}
.foot-brand{position:absolute;left:110px;top:2812px;font-weight:700;font-size:26px;color:#fff}
.foot-text{position:absolute;left:110px;top:2876px;width:280px;font-size:12.5px;line-height:25px;color:#fff}
.foot-head{position:absolute;top:2810px;font-size:17px;font-weight:600;color:#fff}
.foot-links{position:absolute;top:2877px;list-style:none;font-size:14.5px;color:#fff;line-height:29px}
.foot-links li::before{content:"»";margin-right:9px}
.foot-phone-icon{position:absolute;left:885px;top:2886px;width:42px;height:42px;border:1.5px solid #ddd;border-radius:50%}
.foot-phone-icon svg{position:absolute;left:12px;top:12px}
.foot-phone{position:absolute;left:938px;top:2895px;font-size:17px;color:#fff}
.social{position:absolute;top:2942px;width:34px;height:34px;border:1.5px solid #ddd}
.social i{position:absolute;left:10px;top:10px;width:11px;height:11px;background:#fff}
.copyright{position:absolute;top:3106px;font-size:14.5px;font-weight:500;color:#fff}
</style>
</head>
<body>

<header class="site-header">
  <div class="brand">Velvet Basin Suites</div>
  <div class="nav active" style="left:453px">Home</div>
  <div class="nav" style="left:528px">Events</div>
  <div class="nav" style="left:607px">Products</div>
  <div class="nav" style="left:703px">Contact Us</div>
  <div class="call-icon"><svg width="16" height="16" viewBox="0 0 24 24"><path fill="#2a5196" d="M6.6 10.8a15 15 0 0 0 6.6 6.6l2.2-2.2a1 1 0 0 1 1-.25 11.4 11.4 0 0 0 3.6.57 1 1 0 0 1 1 1V20a1 1 0 0 1-1 1A17 17 0 0 1 3 4a1 1 0 0 1 1-1h3.5a1 1 0 0 1 1 1c0 1.25.2 2.45.57 3.57a1 1 0 0 1-.25 1z"/></svg></div>
  <div class="call-text">Call Now - +1 (555) 014 2277</div>
</header>

<section class="hero">
  <div class="hero-cell" role="img" aria-label="Rows of portable toilets on a green field" style="left:0;top:8px;width:235px;height:257px;background:linear-gradient(180deg,#8fb3d8,#3e6b2c 70%,#557d37)"></div>
  <div class="hero-cell" role="img" aria-label="Yellow portable toilets under blue sky" style="left:241px;top:8px;width:235px;height:257px;background:linear-gradient(180deg,#4f74a8,#a68c2a 75%,#6a5c2a)"></div>
  <div class="hero-cell" role="img" aria-label="Blue portable units beside city skyline" style="left:482px;top:8px;width:235px;height:257px;background:linear-gradient(180deg,#6f94c4,#33558f)"></div>
  <div class="hero-cell" role="img" aria-label="Service truck at a work site" style="left:723px;top:8px;width:235px;height:257px;background:linear-gradient(180deg,#b9452f,#6d6a5e)"></div>
  <div class="hero-cell" role="img" aria-label="Green portable toilet at a construction site" style="left:964px;top:8px;width:236px;height:257px;background:linear-gradient(180deg,#b9c8da,#c9b79a)"></div>
  <div class="hero-cell" role="img" aria-label="Long row of blue portable toilets" style="left:0;top:271px;width:235px;height:257px;background:linear-gradient(180deg,#4d86b8,#1d5c95)"></div>
  <div class="hero-cell" role="img" aria-label="White restroom trailer" style="left:241px;top:271px;width:235px;height:257px;background:linear-gradient(180deg,#7d7f82,#d8d8d6)"></div>
  <div class="hero-cell" role="img" aria-label="Worker handling a portable unit" style="left:482px;top:271px;width:235px;height:257px;background:linear-gradient(180deg,#6f8da4,#1c7a6e)"></div>
  <div class="hero-cell" role="img" aria-label="Red portable toilets in a park" style="left:723px;top:271px;width:477px;height:257px;background:linear-gradient(180deg,#3d5e35,#b32b25 45%,#4c7a31)"></div>
  <div class="hero-overlay"></div>
  <div class="hero-title center">Velvet Basin Suites</div>
  <p class="hero-text">Lorem ipsum dolor sit amet, consectetur adipiscing elit, sed do eiusmod tempor incididunt ut labore et dolore magna aliqua. Ut enim ad minim veniam</p>
  <div class="btn-start">Get Started <svg width="16" height="10" viewBox="0 0 16 10"><path d="M0 5h13M9 1l4 4-4 4" stroke="#fff" stroke-width="2" fill="none"/></svg></div>
</section>

<!-- events -->
<h2 class="sec-title center" style="top:686px">Events</h2>
<div class="sec-rule" style="top:746px"></div>
<p class="sec-text" style="top:772px">Lorem ipsum dolor sit amet, consectetur adipiscing elit, sed do eiusmod tempor incididunt ut labore et dolore magna aliqua. Ut enim ad minim veniam, quis nostrud exercitation ullamco</p>

<div class="arrow-btn" style="left:48px"><svg width="12" height="14" viewBox="0 0 12 14"><path d="M8 1 2 7l6 6" stroke="#333" stroke-width="2" fill="none"/></svg></div>
<div class="arrow-btn" style="left:1106px"><svg width="12" height="14" viewBox="0 0 12 14"><path d="m4 1 6 6-6 6" stroke="#333" stroke-width="2" fill="none"/></svg></div>

<div class="event-card" role="img" aria-label="Wedding couple with bouquet" style="left:111px;background:linear-gradient(160deg,#5a5348,#2b2a27 60%,#c8b8a6)"></div>
<div class="event-card" role="img" aria-label="Friends at a private boat party" style="left:359px;background:linear-gradient(160deg,#9ab0c2,#6a6256 55%,#ded7cb)"></div>
<div class="event-card" role="img" aria-label="Festival crowd at sunset" style="left:607px;background:linear-gradient(160deg,#cfe4ee,#e2a35c 55%,#7a3b2a)"></div>
<div class="event-card" role="img" aria-label="Family reunion dinner under string lights" style="left:855px;background:linear-gradient(160deg,#3a2e25,#6b4a33 55%,#2b2420)"></div>
<div class="event-name" style="left:111px">Weddings</div>
<div class="event-name" style="left:359px">Private Parties</div>
<div class="event-name" style="left:607px">Festivals</div>
<div class="event-name" style="left:855px">Family Reunions</div>

<!-- products -->
<div class="products-band" role="img" aria-label="Blue tinted row of portable toilets"></div>
<h2 class="sec-title center" style="top:1309px;color:#fff">Products</h2>
<div class="sec-rule" style="top:1369px;background:#fff"></div>
<p class="sec-text" style="top:1395px;color:#fff">Lorem ipsum dolor sit amet, consectetur adipiscing elit, sed do eiusmod tempor incididunt ut labore et dolore magna aliqua. Ut enim ad minim veniam, quis nostrud exercitation ullamco</p>

<div class="product-card" style="left:111px">
  <div class="product-img" role="img" aria-label="Blue portable toilet" style="left:108px;width:96px;height:176px;background:linear-gradient(180deg,#2f6fd0,#1447a8)"></div>
  <div class="product-name">Product 1</div>
  <p class="product-text">Lorem ipsum dolor sit amet, consectetur adipiscing elit, sed do eiusmod incididunt ut labore et dolore magna aliqua.</p>
</div>
<div class="product-card" style="left:444px">
  <div class="product-img" role="img" aria-label="White restroom trailer unit" style="left:22px;width:267px;height:176px;background:linear-gradient(180deg,#e6e8ea,#a9acae 75%,#5e5a55)"></div>
  <div class="product-name">Product 2</div>
  <p class="product-text">Lorem ipsum dolor sit amet, consectetur adipiscing elit, sed do eiusmod incididunt ut labore et dolore magna aliqua.</p>
</div>
<div class="product-card" style="left:775px">
  <div class="product-img" role="img" aria-label="Row of teal and white portable toilets" style="left:12px;top:38px;width:287px;height:130px;background:linear-gradient(90deg,#1d6f78,#e3e7e7 30%,#1d6f78 60%,#dfe4e4)"></div>
  <div class="product-name">Product 3</div>
  <p class="product-text">Lorem ipsum dolor sit amet, consectetur adipiscing elit, sed do eiusmod incididunt ut labore et dolore magna aliqua.</p>
</div>
<div class="dot" style="left:567px"></div>
<div class="dot" style="left:584px"></div>
<div class="dot on" style="left:601px"></div>
<div class="dot" style="left:618px"></div>

<!-- contact -->
<h2 class="sec-title center" style="top:2003px">Contact Us</h2>
<div class="sec-rule" style="top:2064px"></div>
<p class="sec-text" style="top:2089px">Lorem ipsum dolor sit amet, consectetur adipiscing elit, sed do eiusmod tempor incididunt ut labore et dolore magna aliqua. Ut enim ad minim veniam, quis nostrud exercitation ullamco</p>

<form>
  <div class="field" style="left:227px;top:2156px;width:350px"><span>Name</span></div>
  <div class="field" style="left:623px;top:2156px;width:350px"><span>Email Address</span></div>
  <div class="field" style="left:227px;top:2226px;width:350px"><span>Phone Number</span></div>
  <div class="field" style="left:623px;top:2226px;width:350px"><span>Type Of Event</span><svg width="10" height="6"><path d="M0 0h10L5 6z" fill="#444"/></svg></div>
  <div class="field" style="left:227px;top:2294px;width:350px"><span>How many peoples</span><svg width="10" height="6"><path d="M0 0h10L5 6z" fill="#444"/></svg></div>
  <div class="field" style="left:623px;top:2294px;width:350px"><span>Type of product your interested in</span><svg width="10" height="6"><path d="M0 0h10L5 6z" fill="#444"/></svg></div>
  <div class="field" style="left:227px;top:2365px;width:350px"><span>When do you need it</span><svg width="10" height="6"><path d="M0 0h10L5 6z" fill="#444"/></svg></div>
  <div class="field" style="left:623px;top:2365px;width:350px"><span>For how long</span><svg width="10" height="6"><path d="M0 0h10L5 6z" fill="#444"/></svg></div>
  <div class="field" style="left:227px;top:2437px;width:741px"><span>Where</span><svg width="10" height="13" viewBox="0 0 10 13"><path d="M5 0a5 5 0 0 1 5 5c0 3-5 8-5 8S0 8 0 5a5 5 0 0 1 5-5z" fill="#444"/><circle cx="5" cy="5" r="2" fill="#fff"/></svg></div>
  <div class="field" style="left:227px;top:2508px;width:741px;height:114px"><span>Message</span></div>
  <div class="btn-send">SEND MESSAGE</div>
</form>

<!-- footer -->
<footer class="site-footer"></footer>
<div class="foot-brand">Velvet Basin Suites</div>
<p class="foot-text">Lorem ipsum dolor sit amet, adipiscing elit, sed do eiusmod tempor incididunt ut labore et dolore magna aliqua. Ut enim ad minim veniam</p>

<div class="foot-head" style="left:513px">QUICK LINKS</div>
<ul class="foot-links" style="left:513px"><li>Home</li><li>Events</li><li>Products</li><li>Contact</li></ul>

<div class="foot-head" style="left:688px">EVENTS</div>
<ul class="foot-links" style="left:688px"><li>Weddings</li><li>Private Parties</li><li>Festivals</li><li>Family Reunions</li><li>Team Building</li><li>Wine Tastings</li></ul>

<div class="foot-head" style="left:880px">CONTACT US</div>
<div class="foot-phone-icon"><svg width="17" height="17" viewBox="0 0 24 24"><path fill="none" stroke="#fff" stroke-width="1.6" d="M6.6 10.8a15 15 0 0 0 6.6 6.6l2.2-2.2a1 1 0 0 1 1-.25 11.4 11.4 0 0 0 3.6.57 1 1 0 0 1 1 1V20a1 1 0 0 1-1 1A17 17 0 0 1 3 4a1 1 0 0 1 1-1h3.5a1 1 0 0 1 1 1c0 1.25.2 2.45.57 3.57a1 1 0 0 1-.25 1z"/></svg></div>
<div class="foot-phone">+1 (555) 014 2277</div>
<div class="social" style="left:891px"><i></i></div>
<div class="social" style="left:937px"><i></i></div>
<div class="social" style="left:984px"><i></i></div>
<div class="social" style="left:1030px"><i></i></div>

<div class="copyright center">Velvet Basin Suites, © 2022 All Rights Reserved</div>

</body>
</html>
```